Regional Showdown Flyer for Holiday Program

Need a one page flyer, can be back to front or one page, ensuring you can fit all information, colourful, aimed at a market of 8-13 year old boys and girls.
The flyer needs to be noticed, needs to have certain information on it and needs to be Autralian Rule Football orientated.
Have uploaded file so you can understand the style (not content), style of flyer I am looking at getting submitted.

Target Market(s)

8-13 year old boys and girls and their parents.

Requirements
Must have
• Regional Showdown Event
• Price for Regional Showdown Day will be $85
• Strictly Limited Places, only the best footballers should enter this challenge
• Inaugural event, be the first Regional Showdown Winner for your age!
• Do you love a challenge! Put yourself to the test!
• Are you up to it - Water Slide Goal Kicking Contest! The fastest kick in the West (tested by our very own speed gun)! Can you survive the Footy Titan Trail or Last One Standing Goal Kicking! These challenges are crazy are super fun!
• If you think you can deliver on the big stage then this is for YOU!
• All District age winners will receive prizes, awards and the adulation from all their peers!
• Year's 3-5 from 9am to 12pm
• Year's 6-8 from 1-4pm
• All challengers compete against their own age
• Lunch Provided
• Monday 16th April - Upper Tarrowby Regional Showdown Day at Tarrowby Oval
• Tuesday 17th April - North Tarrowby Regional Showdown Day at Kilmorna Reserve
• Wednesday 18th April - Yarlo Regional Showdown Day - Dunhaven Football Club
• Every Challenge Participant receives a District Football!
• Need to put all 3 District Football Logos on the bottom of the flyer, logos attached at bottom.
Nice to have
• Plenty of colour, if you can fit all information on one page that would be fine
Should not have
• Dull, boring, any footballs should be Aussie Rules footballs not NFL or soccer

```html
<!DOCTYPE html>
<html lang="en">
<head>
<meta charset="utf-8">
<title>Regional Showdown Event Flyer</title>
<link rel="stylesheet" href="https://fonts.googleapis.com/css2?family=Lilita+One&family=Oswald:wght@400;500;600&family=Roboto+Condensed:wght@400;700&display=swap">
<style>
:root{
  --navy:#17315f;
  --blue-deep:#1b4d8f;
  --blue-mid:#2477c4;
  --green-deep:#15603a;
  --red:#e3232c;
  --orange:#ee8a1c;
  --sky:#2aa3dc;
  --green:#35a845;
  --grey:#b9bcc0;
  --light-blue:#7cc9f0;
  --yellow:#ffd23f;
  --white:#ffffff;
  --bg:#ececec;
  --ball:#8a3b1c;
}
*{margin:0;padding:0;box-sizing:border-box}
html,body{width:1200px;height:913px;overflow:hidden;background:var(--bg)}
body{position:relative;font-family:"Roboto Condensed",sans-serif;color:var(--white)}
.page{position:absolute;top:46px;width:560px;height:820px;overflow:hidden;box-shadow:0 6px 20px rgba(0,0,0,.25)}
.page--front{left:30px;background:linear-gradient(180deg,var(--blue-deep) 0%,var(--blue-mid) 55%,var(--green-deep) 100%)}
.page--back{left:610px;background:linear-gradient(180deg,var(--blue-deep) 0%,var(--blue-mid) 70%,var(--blue-deep) 100%)}
.layer{position:absolute;left:0;top:0}
.title{position:absolute;left:0;width:100%;text-align:center;font-family:"Lilita One",sans-serif;color:var(--red);line-height:.95;font-size:48px;-webkit-text-stroke:1.5px var(--white);text-shadow:2px 3px 0 rgba(0,0,0,.35)}
.page--back .title{-webkit-text-stroke:0;text-shadow:none}
.inaugural{position:absolute;left:300px;top:200px;width:250px;text-align:center}
.inaugural__head{font-family:"Oswald",sans-serif;font-weight:500;color:var(--light-blue);font-size:32px;letter-spacing:.5px}
.inaugural__sub{font-family:"Oswald",sans-serif;font-size:18px;line-height:1.2}
.challenge{position:absolute;left:28px;top:468px;font-family:"Lilita One",sans-serif;font-size:27px;line-height:1.1;text-shadow:1px 2px 2px rgba(0,0,0,.3)}
.upto{position:absolute;left:330px;top:508px;font-family:"Oswald",sans-serif;font-size:17px}
.ribbon{position:absolute;font-family:"Oswald",sans-serif;font-weight:500;text-align:center;box-shadow:2px 3px 5px rgba(0,0,0,.3);white-space:nowrap;font-size:16px;padding:6px 8px}
.ribbon small{font-size:10.5px;font-weight:400}
.ribbon--orange{left:290px;top:540px;width:250px;background:var(--orange)}
.ribbon--blue{left:110px;top:580px;width:435px;background:var(--sky)}
.ribbon--green{left:180px;top:622px;width:360px;background:var(--green);line-height:1.2}
.crazy{position:absolute;left:230px;top:690px;width:310px;text-align:right;font-family:"Lilita One",sans-serif;font-size:23px;line-height:1.1}
.bigstage{position:absolute;left:200px;top:755px;width:345px;text-align:right;font-family:"Oswald",sans-serif;font-size:19px;color:var(--green);line-height:1.2}
.dates{position:absolute;left:180px;top:250px;width:380px}
.date{padding:5px 14px;text-align:center;line-height:1.12}
.date__day{font-family:"Oswald",sans-serif;font-size:17px}
.date__day b{font-weight:600}
.date__place{font-family:"Oswald",sans-serif;font-size:15px}
.date--orange{background:var(--orange)}
.date--blue{background:var(--sky)}
.date--green{background:var(--green)}
.date--grey{background:var(--grey);color:var(--navy);font-size:14px;padding:7px 14px}
.date + .date{margin-top:5px}
.details{position:absolute;left:24px;top:530px;width:512px;font-family:"Oswald",sans-serif;font-size:15px;line-height:1.35;text-align:right}
.details__price{font-size:22px;font-weight:600;color:var(--yellow)}
.details b{font-weight:600}
.footer{position:absolute;left:24px;top:688px;width:512px;text-align:right}
.footer__lead{font-size:13px}
.footer__web{font-family:"Oswald",sans-serif;font-size:20px;font-weight:500}
.clubs{position:absolute;left:0;bottom:0;width:100%;height:58px;background:var(--white);display:flex;justify-content:space-around;align-items:center}
.club{display:flex;align-items:center;gap:8px;font-family:"Oswald",sans-serif;font-weight:500;font-size:16px;color:var(--navy)}
.club__mark{width:22px;height:22px;border-radius:50%;background:var(--navy)}
</style>
</head>
<body>

<section class="page page--front">
  <svg class="layer" width="560" height="820" viewBox="0 0 560 820">
    <defs>
      <linearGradient id="photoTone" x1="0" y1="0" x2="0" y2="1">
        <stop offset="0" stop-color="#6f8fb8"/>
        <stop offset=".55" stop-color="#b9c9d8"/>
        <stop offset=".7" stop-color="#5d8a3c"/>
        <stop offset="1" stop-color="#3f6d2a"/>
      </linearGradient>
    </defs>
    <path d="M0 0H560V130Q300 200 0 140Z" fill="var(--navy)"/>
    <path d="M0 140Q300 200 560 130V145Q300 215 0 160Z" fill="var(--white)"/>
    <path role="img" aria-label="Photo of a young footballer holding a ball on a grassy field" d="M0 160Q300 215 560 145V330Q460 470 250 430Q110 405 0 420Z" fill="url(#photoTone)"/>
    <path d="M0 420Q110 405 250 430Q460 470 560 330V350Q470 490 250 450Q110 425 0 440Z" fill="var(--white)"/>
    <ellipse role="img" aria-label="Football illustration" cx="90" cy="770" rx="80" ry="36" fill="var(--ball)"/>
  </svg>

  <h1 class="title" style="top:38px">Regional Showdown<br>Event</h1>

  <div class="inaugural">
    <div class="inaugural__head">INAUGURAL EVENT</div>
    <div class="inaugural__sub">Be the first Regional Showdown<br>Winner for your age!</div>
  </div>

  <p class="challenge">Do you love a challenge!<br>Put yourselfto the test!</p>
  <p class="upto">Are you up to it ...</p>

  <div class="ribbon ribbon--orange">Water Slide Goal Kicking Contest!</div>
  <div class="ribbon ribbon--blue">The Fastest Kick in the West! <small>(Tested by our very own speed gun)</small></div>
  <div class="ribbon ribbon--green">Can you survive the Footy Titan Trail<br>or Last One Standing Goal Kicking!</div>

  <p class="crazy">These challenges are crazy...<br>super fun!</p>
  <p class="bigstage">If you think you can deliver on the big stage<br>then this is for YOU!</p>
</section>

<section class="page page--back">
  <svg class="layer" width="560" height="820" viewBox="0 0 560 820">
    <path d="M0 0H560V130Q300 170 0 110Z" fill="var(--white)"/>
    <path d="M0 110Q300 170 560 130V150Q300 195 0 128Z" fill="var(--navy)"/>
    <ellipse role="img" aria-label="Football illustration" cx="90" cy="290" rx="60" ry="28" fill="var(--ball)"/>
  </svg>

  <h2 class="title" style="top:28px">Regional Showdown<br>Event</h2>

  <div class="dates">
    <div class="date date--orange">
      <div class="date__day">Monday | <b>16<sup>th</sup> April</b></div>
      <div class="date__place">Upper Tarrowby Regional<br>Showdown Day at <b>Tarrowby Oval</b></div>
    </div>
    <div class="date date--blue">
      <div class="date__day">Tuesday | <b>17<sup>th</sup> April</b></div>
      <div class="date__place">North Tarrowby Regional<br>Showdown Day at <b>Kilmorna Reserve</b></div>
    </div>
    <div class="date date--green">
      <div class="date__day">Wednesday | <b>18<sup>th</sup> April</b></div>
      <div class="date__place">Yarlo Regional Showdown Day<br><b>Dunhaven Football Club</b></div>
    </div>
    <div class="date date--grey"><b>Strictly Limited Places.</b><br>Only the best footballers should enter this challenge</div>
  </div>

  <div class="details">
    <div class="details__price">Regional Showdown Day only $85</div>
    <div><b>Year's 3-5</b> 9am to 12pm &nbsp;|&nbsp; <b>Year's 6-8</b> 1pm to 4pm</div>
    <div>All challengers compete against their own age &nbsp;|&nbsp; <b>Lunch Provided</b></div>
    <div>All age winners receive prizes, awards and the adulation of their peers!</div>
    <div><b>Every Challenge Participant receives a District Football!</b></div>
  </div>

  <div class="footer">
    <div class="footer__lead">For more information visit us on</div>
    <div class="footer__web">www.tarrowbyfooty.com.au</div>
  </div>

  <div class="clubs">
    <div class="club"><span class="club__mark"></span>Tarrowby Districts</div>
    <div class="club"><span class="club__mark"></span>Kilmorna Hawks</div>
    <div class="club"><span class="club__mark"></span>Yarlo Juniors</div>
  </div>
</section>

</body>
</html>
```